UNIQUE, Elegant business card for transport company.

MUST BE AN ACTUAL GRAPHIC DESIGNER.
NO TEMPLATES, NO MOCKUP GENERATORS.
Looking for a top notch, head turning, business card.
Will be printed on premium luxury paper with spot glossing and debossing.
Must know how to set up for spot glossing. Must be willing to work on the file to meet printers spec after final design.

Target Market(s)

All info on .psd file

Contact Information for Business Card

All info on .psd file

Requirements
Must have
• All info on .psd file
Nice to have
• All info on .psd file
Should not have
• Nothing red

```html
<!DOCTYPE html>
<html lang="en">
<head>
<meta charset="utf-8">
<title>Business Card – Director</title>
<link rel="stylesheet" href="https://fonts.googleapis.com/css2?family=Montserrat:wght@400;500;600&display=swap">
<style>
  :root {
    --sky: #45bdf8;
    --sky-light: #7fd6fb;
    --sky-pale: #d6f3fe;
    --ink: #070909;
    --name-blue: #4cbcf4;
    --title-blue: #3b8fdc;
    --contact-blue: #57bff3;
    --page: #ffffff;
  }
  * { margin: 0; padding: 0; box-sizing: border-box; }
  html, body {
    width: 1200px; height: 686px; overflow: hidden;
    background: var(--page);
    font-family: "Montserrat", sans-serif;
  }
  .card {
    position: relative;
    width: 1200px; height: 686px;
    border-radius: 22px;
    overflow: hidden;
    background: var(--sky);
  }
  .card__wave { position: absolute; inset: 0; width: 1200px; height: 686px; }
  .identity { position: absolute; left: 41px; top: 250px; }
  .identity__name {
    font-weight: 600; font-size: 44px; line-height: 1.1;
    color: var(--name-blue); letter-spacing: 0.5px;
  }
  .identity__title {
    font-weight: 400; font-size: 31px; line-height: 1.1;
    color: var(--title-blue); letter-spacing: 0.5px;
  }
  .address {
    position: absolute; left: 43px; top: 356px;
    font-style: normal; font-size: 33px; line-height: 38px;
    color: var(--title-blue); letter-spacing: 0.6px;
  }
  .contacts { position: absolute; left: 43px; top: 462px; list-style: none; }
  .contacts__item {
    display: flex; align-items: center; gap: 13px;
    height: 48.5px;
    font-size: 30px; color: var(--contact-blue); letter-spacing: 0.6px;
  }
  .contacts__icon { width: 30px; height: 30px; flex: none; fill: var(--contact-blue); }
  .vehicle-mark {
    position: absolute; left: 858px; top: 262px;
    width: 268px; height: 378px;
    border-radius: 40px;
    background: radial-gradient(ellipse at 50% 40%, #f2f6f8 0%, #8fd4f6 35%, #2f9ee6 70%, #0b2a3d 100%);
  }
</style>
</head>
<body>
<main class="card">
  <svg class="card__wave" viewBox="0 0 1200 686" aria-hidden="true">
    <path d="M0 180 C120 90 320 30 520 70 C650 100 760 170 900 200 C1020 222 1120 200 1200 160 V250 H0 Z" fill="var(--sky-light)" opacity="0.55"/>
    <path d="M600 150 C760 215 900 235 1020 220 C1100 210 1160 185 1200 160 L1200 200 C1120 240 1000 250 880 238 C780 228 690 195 600 150 Z" fill="var(--sky-pale)" opacity="0.7"/>
    <path d="M0 686 V205 C70 125 190 55 330 52 C520 48 690 190 890 228 C1020 252 1120 238 1200 210 V686 Z" fill="var(--ink)"/>
    <path d="M0 168 C110 80 260 40 420 55 C480 62 530 78 560 92 C500 72 440 66 380 68 C240 76 100 130 0 200 Z" fill="var(--sky-light)"/>
  </svg>

  <header class="identity">
    <h1 class="identity__name">Your Name</h1>
    <p class="identity__title">Director</p>
  </header>

  <address class="address">12 Larkspur Court,<br>Brookvale NSW 2160</address>

  <ul class="contacts">
    <li class="contacts__item">
      <svg class="contacts__icon" viewBox="0 0 24 24" aria-hidden="true"><path d="M3 8c0-2 3-4 9-4s9 2 9 4v2h-4V8.5c-1.5-.6-3-.8-5-.8s-3.5.2-5 .8V10H3z M6 12h12l2 7H4z M10 14h4v3h-4z" /></svg>
      <span>1234 456 789</span>
    </li>
    <li class="contacts__item">
      <svg class="contacts__icon" viewBox="0 0 24 24" aria-hidden="true"><path d="M6.6 10.8c1.4 2.8 3.8 5.1 6.6 6.6l2.2-2.2c.3-.3.7-.4 1-.2 1.1.4 2.3.6 3.6.6.6 0 1 .4 1 1V20c0 .6-.4 1-1 1C10.6 21 3 13.4 3 4c0-.6.4-1 1-1h3.5c.6 0 1 .4 1 1 0 1.3.2 2.5.6 3.6.1.3 0 .7-.2 1z M14 3h2a5 5 0 0 1 5 5v2h-2V8a3 3 0 0 0-3-3h-2z M14 7h1a2 2 0 0 1 2 2v1h-2V9h-1z"/></svg>
      <span>1234 456 789</span>
    </li>
    <li class="contacts__item">
      <svg class="contacts__icon" viewBox="0 0 24 24" aria-hidden="true"><path d="M2 5h20v14H2z M3.5 6.5 12 13l8.5-6.5z" fill-rule="evenodd"/></svg>
      <span>yourmail@example.com</span>
    </li>
    <li class="contacts__item">
      <svg class="contacts__icon" viewBox="0 0 24 24" aria-hidden="true"><circle cx="12" cy="12" r="10"/><path d="M7 6c2 1 3 2 2 4s1 3 2 4-1 3-2 4M15 4c-1 2 1 3 2 3s2 2 1 4-2 3-1 5" stroke="var(--ink)" stroke-width="1.6" fill="none"/></svg>
      <span>younamerwebsite.com</span>
    </li>
  </ul>

  <div class="vehicle-mark" role="img" aria-label="Illustration of a white delivery van inside a blue location pin with concentric rings below"></div>
</main>
</body>
</html>
```